spot uv business card design for QRT Mechanics

I need a great new business card design best suited for spot uv printing. Details to include are Desmond Hollis 0491227305 wwwqrtmech.com.au, des@qrtmech.com.au. Company logo attached.
The design has to be spot uv/varnish optimised!!
Business

```html
<!DOCTYPE html>
<html lang="en">
<head>
<meta charset="utf-8">
<title>QRT Mechanics – Business Card</title>
<link href="https://fonts.googleapis.com/css2?family=Open+Sans:wght@300;400&display=swap" rel="stylesheet">
<style>
  :root {
    --page-bg: #2a2a2c;
    --card-front: #000000;
    --card-back: #2e5676;
    --brand-blue: #3f6d93;
    --text-light: #ffffff;
  }
  * { margin: 0; padding: 0; box-sizing: border-box; }
  html, body {
    width: 1200px;
    height: 926px;
    overflow: hidden;
    background: var(--page-bg);
    font-family: "Open Sans", sans-serif;
  }
  .sheet {
    position: relative;
    width: 1200px;
    height: 926px;
  }
  .card {
    position: absolute;
    left: 250px;
    width: 700px;
    height: 400px;
  }
  .card--front {
    top: 42px;
    background: var(--card-front);
    display: flex;
    align-items: center;
    justify-content: center;
  }
  .card--back {
    top: 484px;
    background: var(--card-back);
    color: var(--text-light);
  }
  .brand {
    display: flex;
    align-items: center;
    gap: 18px;
    color: var(--brand-blue);
  }
  .brand__mark {
    width: 34px;
    height: 34px;
    background: var(--brand-blue);
  }
  .brand__name {
    font-weight: 300;
    font-size: 52px;
    letter-spacing: 1px;
    text-transform: uppercase;
  }
  .holder-name {
    position: absolute;
    left: 150px;
    top: 130px;
    font-weight: 300;
    font-size: 40px;
    letter-spacing: 1px;
  }
  .contact-list {
    position: absolute;
    left: 36px;
    right: 36px;
    bottom: 52px;
    display: flex;
    justify-content: space-between;
    list-style: none;
    font-size: 17px;
    font-weight: 400;
  }
  .contact-list__item {
    display: flex;
    align-items: center;
    gap: 6px;
  }
  .contact-list__icon {
    width: 18px;
    height: 16px;
    fill: var(--text-light);
  }
</style>
</head>
<body>
<main class="sheet">
  <section class="card card--front" aria-label="Card front">
    <div class="brand">
      <span class="brand__mark"></span>
      <span class="brand__name">QRT Mechanics</span>
    </div>
  </section>

  <section class="card card--back" aria-label="Card back">
    <h1 class="holder-name">Desmond Hollis</h1>
    <ul class="contact-list">
      <li class="contact-list__item">
        <svg class="contact-list__icon" viewBox="0 0 18 16" aria-hidden="true">
          <path d="M2 4c0-2 2-3 7-3s7 1 7 3v1h-4V4H6v1H2z"/>
          <rect x="3" y="6" width="12" height="9" rx="1"/>
        </svg>
        049-122-7305
      </li>
      <li class="contact-list__item">
        <svg class="contact-list__icon" viewBox="0 0 18 16" aria-hidden="true">
          <path d="M1 1h16v11H1z M3 3v7h12V3z" fill-rule="evenodd"/>
          <rect x="6" y="13" width="6" height="2"/>
        </svg>
        www.qrtmech.com.au
      </li>
      <li class="contact-list__item">
        <svg class="contact-list__icon" viewBox="0 0 18 16" aria-hidden="true">
          <path d="M1 2h16v12H1z M2.5 3.5 9 9l6.5-5.5z" fill-rule="evenodd"/>
        </svg>
        des@qrtmech.com.au
      </li>
    </ul>
  </section>
</main>
</body>
</html>
```